Stationary Design Letterhead and Envelope

Artist should provide Letterhead and envelop stationary designs

Info for stationary:
Fenwarde Outdoor Advertising
4857 Mesa Rd. 318 N. PO BOX 582917
Austin, TX 78651

Dale Fenwarde
President
512-608-2917
dale@fenwardeoutdoor.example
fenwardeoutdoor.example

Target Market(s)

clients

Colors
0054AA
0677BA
7BADD7
CADEEF
E8F1F8

Requirements
Must have
• high quality unique eye catching and dynamic

```html
<!DOCTYPE html>
<html lang="en">
<head>
<meta charset="utf-8">
<title>Fenwarde Outdoor Advertising — Letterhead</title>
<link rel="stylesheet" href="https://fonts.googleapis.com/css2?family=Montserrat:wght@400;600;700&family=Lato:wght@400;700&family=Dancing+Script:wght@500&display=swap">
<style>
  :root {
    --brand-blue: #0677BA;
    --deep-blue: #0054AA;
    --ink: #2b2b2b;
    --ink-soft: #444;
    --black: #111;
    --paper: #ffffff;
    --backdrop: #e9e9ea;
  }
  * { box-sizing: border-box; margin: 0; padding: 0; }
  html, body {
    width: 1200px; height: 960px; overflow: hidden;
    background: var(--backdrop);
  }
  .letterhead {
    position: absolute; left: 260px; top: 40px;
    width: 680px; height: 880px;
    background: var(--paper);
    box-shadow: 0 6px 24px rgba(0,0,0,.12);
    overflow: hidden;
    font-family: "Lato", sans-serif;
    color: var(--ink);
  }
  .brand {
    position: absolute; left: 58px; top: 118px;
    display: flex; align-items: center; gap: 12px;
    width: 300px;
  }
  .brand-square { width: 26px; height: 26px; background: var(--brand-blue); flex: none; }
  .brand-name {
    font-family: "Montserrat", sans-serif; font-weight: 700;
    font-size: 18px; line-height: 1.2; letter-spacing: .5px; color: var(--black);
    text-transform: uppercase;
  }
  .brand-name span { display: block; }
  .contact {
    position: absolute; left: 400px; top: 40px; height: 143px;
    padding-left: 14px;
    border-left: 1.5px solid var(--brand-blue);
    font-family: "Montserrat", sans-serif; font-size: 9.5px; line-height: 1.45;
    color: var(--ink-soft);
  }
  .contact-name { color: var(--brand-blue); font-weight: 700; font-size: 10px; text-transform: uppercase; }
  .contact-row { display: flex; align-items: center; gap: 6px; }
  .contact-row svg { width: 9px; height: 9px; fill: var(--brand-blue); flex: none; }
  .header-rule {
    position: absolute; left: 150px; right: 52px; top: 182px;
    height: 1.5px; background: var(--brand-blue);
  }
  .letter { position: absolute; left: 86px; top: 225px; width: 520px; font-size: 12.5px; line-height: 1.5; }
  .letter-date { margin-bottom: 16px; }
  .recipient { margin-bottom: 16px; }
  .salutation { font-family: "Montserrat", sans-serif; font-weight: 700; font-size: 15px; margin-bottom: 14px; }
  .letter p.body { margin-bottom: 16px; }
  .closing { margin-top: 22px; }
  .signature {
    font-family: "Dancing Script", cursive; font-size: 40px; font-weight: 500;
    color: var(--ink); margin: 10px 0 0 20px;
  }
  .swoosh { position: absolute; inset: 0; width: 680px; height: 880px; pointer-events: none; }
  .swoosh .band { fill: var(--brand-blue); }
  .swoosh .accent { fill: var(--black); }
</style>
</head>
<body>
  <div class="letterhead">
    <div class="brand">
      <span class="brand-square"></span>
      <span class="brand-name"><span>Fenwarde</span><span>Outdoor Advertising</span></span>
    </div>

    <div class="contact">
      <div class="contact-name">Dale Fenwarde</div>
      <div>President</div>
      <div>Fenwarde Outdoor Advertising</div>
      <div>4857 Mesa Rd. 318 N. PO BOX 582917</div>
      <div>Austin, TX 78651</div>
      <div class="contact-row"><svg viewBox="0 0 10 10"><path d="M2 0.5 L3.6 0.5 L4.3 2.8 L3.2 3.8 Q4.2 5.9 6.2 6.8 L7.2 5.7 L9.5 6.4 L9.5 8 Q9.5 9.5 8 9.5 Q1 9 0.5 2 Q0.5 0.5 2 0.5Z"/></svg>512-608-2917</div>
      <div class="contact-row"><svg viewBox="0 0 10 10"><path d="M0 2 L10 2 L10 8.5 L0 8.5Z M0.6 2.4 L5 5.6 L9.4 2.4" stroke="#fff" stroke-width=".8"/></svg>dale@fenwardeoutdoor.example</div>
      <div class="contact-row"><svg viewBox="0 0 10 10"><circle cx="5" cy="5" r="4.6"/></svg>fenwardeoutdoor.example</div>
    </div>

    <div class="header-rule"></div>

    <div class="letter">
      <div class="letter-date">January-03-2020</div>
      <div class="recipient">Mr. Peter Vance<br>President</div>
      <div class="recipient">Harlow Corporation<br>123 Street Name, Suite# 10<br>City, State, 120023</div>
      <div class="salutation">Dear Mr. Peter</div>
      <p class="body">Lorem ipsum dolor sit amet, consectetur adipisicing elit, sed do eiusmod tempor incididunt ut labore et dolore magna aliqua. Ut enim ad minim veniam, quis nostrud exercitation ullamco laboris nisi ut aliquip ex ea commodo consequat. Duis aute irure dolor in reprehenderit in voluptate velit esse cillum dolore eu fugiat nulla pariatur.</p>
      <p class="body">Lorem ipsum dolor sit amet, consectetur adipisicing elit, sed do eiusmod tempor incididunt ut labore et dolore magna aliqua. Ut enim ad minim veniam, quis nostrud exercitation ullamco laboris nisi ut aliquip ex ea commodo consequat. Duis aute irure dolor in reprehenderit in voluptate velit esse cillum dolore eu fugiat nulla pariatur.</p>
      <p class="body">Lorem ipsum dolor sit amet, consectetur adipisicing elit, sed do eiusmod tempor incididunt ut labore et dolore magna aliqua. Ut enim ad minim veniam, quis nostrud exercitation ullamco laboris nisi ut aliquip ex ea commodo consequat.</p>
      <p class="body">Excepteur sint occaecat cupidatat non proident, sunt in culpa qui officia deserunt mollit anim id est laborum. re et dolore magnam aliquam quaerat voluptatem.</p>
      <div class="closing">Regards</div>
      <div class="signature">Warren Ashby</div>
    </div>

    <svg class="swoosh" viewBox="0 0 680 880" aria-hidden="true">
      <path class="band" d="M0 880 C300 872 560 830 680 722 L680 880 Z"/>
      <path class="accent" d="M340 838 C500 812 610 770 668 700 L680 706 C620 778 505 820 340 838 Z"/>
    </svg>
  </div>
</body>
</html>
```